Business Card Design

This is a new business We need a business card that shows that we can do whatever people require for maintaining a building we all so like to Achieve a green star feel about the card and Eco Friendly Properly maintenance Building & Construction cleaning,Carpet Cleaning ,Pressure Cleaning Move in Move Out CleaningRubbish RemovalLawn Mowing & Edging>Who we serveCommercial DevelopersResidential BuildersProperty ManagersBuilding Owners Home Owners Real Estate Agents

Target Market(s)

Building & construction

Industry/Entity Type

Property Maintenance

Contact Information for Business Card

Lindenfall Property Maintenance Colin Marsworth Unit 3 / 8 Tamble Road Hastings 3915Victoria Australia Ph 0487365902

Font styles to use
Sans Serif
Script

Colors
9ccb3b
aaaaaa

Requirements
Must have
• Have eco friendly feel

```html
<!DOCTYPE html>
<html lang="en">
<head>
<meta charset="utf-8">
<title>Lindenfall Property Maintenance – Business Card</title>
<link rel="stylesheet" href="https://fonts.googleapis.com/css2?family=Source+Sans+3:wght@400;600;700&display=swap">
<style>
  :root {
    --eco-green: #9ccb3b;
    --ink: #2b2b2b;
    --paper: #ffffff;
    --stage-top: #2a2a2a;
    --stage-bottom: #050505;
  }
  * { box-sizing: border-box; margin: 0; padding: 0; }
  html, body { width: 1200px; height: 900px; overflow: hidden; }
  body {
    position: relative;
    background: linear-gradient(180deg, var(--stage-top) 0%, #161616 55%, var(--stage-bottom) 100%);
    font-family: "Source Sans 3", sans-serif;
  }
  .card {
    position: absolute;
    top: 306px;
    width: 440px;
    height: 271px;
    border-radius: 12px;
  }
  .card--front { left: 149px; background: var(--paper); }
  .card--back { left: 608px; background: var(--eco-green); }

  .brand {
    position: absolute;
    display: flex;
    flex-direction: column;
    align-items: center;
    font-weight: 600;
    line-height: 1.05;
    text-align: center;
  }
  .brand__dot {
    width: 56px;
    height: 56px;
    border-radius: 50%;
    margin-bottom: 12px;
  }
  .brand__name { font-size: 30px; letter-spacing: 0.5px; }
  .brand__tag { font-size: 17px; }

  .card--front .brand { left: 22px; top: 76px; width: 184px; color: var(--eco-green); }
  .card--front .brand__dot { background: var(--eco-green); }
  .card--back .brand { left: 110px; top: 62px; width: 220px; color: var(--paper); }
  .card--back .brand__name { font-size: 36px; }
  .card--back .brand__tag { font-size: 20px; }
  .card--back .brand__dot { background: var(--paper); width: 64px; height: 64px; }

  .contact { position: absolute; left: 234px; top: 86px; color: var(--ink); }
  .contact__name {
    font-size: 16px;
    font-weight: 700;
    color: var(--eco-green);
    margin-bottom: 22px;
  }
  .contact__phone {
    display: flex;
    align-items: center;
    gap: 8px;
    font-size: 12.5px;
    margin-bottom: 10px;
  }
  .contact__phone svg { width: 11px; height: 11px; fill: var(--eco-green); }
  .contact__address { font-size: 12.5px; line-height: 15px; font-style: normal; }
</style>
</head>
<body>
  <section class="card card--front" aria-label="Card front">
    <div class="brand">
      <span class="brand__dot"></span>
      <span class="brand__name">Lindenfall</span>
      <span class="brand__tag">Property Maintenance</span>
    </div>
    <div class="contact">
      <p class="contact__name">Colin Marsworth</p>
      <p class="contact__phone">
        <svg viewBox="0 0 24 24" aria-hidden="true"><path d="M6.6 10.8a15.1 15.1 0 0 0 6.6 6.6l2.2-2.2c.3-.3.7-.4 1-.2 1.1.4 2.3.6 3.6.6.6 0 1 .4 1 1V20c0 .6-.4 1-1 1A17 17 0 0 1 3 4c0-.6.4-1 1-1h3.5c.6 0 1 .4 1 1 0 1.3.2 2.5.6 3.6.1.3 0 .7-.2 1z"/></svg>
        0487365902
      </p>
      <address class="contact__address">Unit 3 / 8 Tamble Road Orvale<br>3862 Victoria Australia</address>
    </div>
  </section>

  <section class="card card--back" aria-label="Card back">
    <div class="brand">
      <span class="brand__dot"></span>
      <span class="brand__name">Lindenfall</span>
      <span class="brand__tag">Property Maintenance</span>
    </div>
  </section>
</body>
</html>
```